hi all

Im after a new age looking business card with my company logo on it

must include these details, I would like the PH and Email to be symbols

If the colours used for card could be kept within the colours used in logo that I have supplied that would be great, if another colour is to be used dark grey would be ok. no light bulbs etc thanks

Details below to be incorporated on card

Damian Holloway

Lic E871302

PH 0219647381

E info@brightvaleelectrical.example.nz

Domestic Commercial Industrial Electricians

```html
<!DOCTYPE html>
<html lang="en">
<head>
<meta charset="utf-8">
<title>Brightvale Electrical – Business Card</title>
<link rel="stylesheet" href="https://fonts.googleapis.com/css2?family=Roboto:wght@300;400;500;700&display=swap">
<style>
  :root {
    --backdrop: #e3e3e3;
    --card: #1e1e1e;
    --card-deep: #262626;
    --brand-blue: #1b78c8;
    --text-grey: #9a9a9a;
    --text-soft: #858585;
  }
  * { margin: 0; padding: 0; box-sizing: border-box; }
  html, body {
    width: 1200px;
    height: 1200px;
    overflow: hidden;
    background: var(--backdrop);
    font-family: "Roboto", sans-serif;
  }
  .canvas { position: relative; width: 1200px; height: 1200px; }

  .card {
    position: absolute;
    top: 299px;
    width: 361px;
    height: 602px;
    background: var(--card);
    overflow: hidden;
  }
  .card--front { left: 202px; }
  .card--back { left: 627px; }

  .bolt-pattern {
    position: absolute;
    left: 0; top: 0;
    width: 100%;
    height: 470px;
    background: linear-gradient(180deg, var(--card-deep) 0%, var(--card-deep) 55%, var(--card) 100%);
  }

  .brand-mark {
    position: absolute;
    left: 50%;
    transform: translateX(-50%);
    border-radius: 50%;
    background: #141414;
  }
  .card--front .brand-mark { top: 410px; width: 72px; height: 72px; }
  .card--back .brand-mark { top: 40px; width: 66px; height: 66px; }

  .wordmark {
    position: absolute;
    left: 0; right: 0;
    text-align: center;
    color: var(--brand-blue);
    font-weight: 700;
    line-height: 1;
  }
  .wordmark__name { display: block; letter-spacing: 2px; }
  .wordmark__sub { display: block; letter-spacing: 6px; margin-top: 6px; }
  .card--front .wordmark { top: 494px; }
  .card--front .wordmark__name { font-size: 40px; }
  .card--front .wordmark__sub { font-size: 13px; }
  .card--back .wordmark { top: 118px; }
  .card--back .wordmark__name { font-size: 36px; }
  .card--back .wordmark__sub { font-size: 12px; }

  .contact { position: absolute; left: 44px; top: 408px; right: 16px; }
  .contact__name {
    color: var(--brand-blue);
    font-weight: 700;
    font-size: 21px;
    letter-spacing: -0.2px;
    line-height: 24px;
  }
  .contact__licence {
    color: var(--text-grey);
    font-size: 14px;
    line-height: 18px;
    margin-top: 2px;
  }
  .contact__lines { margin-top: 20px; }
  .contact__line {
    color: var(--text-grey);
    font-size: 15px;
    line-height: 20px;
    white-space: nowrap;
  }
  .contact__label { color: var(--brand-blue); }
  .contact__rule {
    width: 28px;
    height: 2px;
    background: var(--brand-blue);
    margin-top: 18px;
  }
  .contact__services {
    color: var(--text-soft);
    font-weight: 300;
    font-size: 12.5px;
    line-height: 15px;
    margin-top: 16px;
    text-transform: uppercase;
  }
</style>
</head>
<body>
<div class="canvas">
  <section class="card card--front" aria-label="Business card front">
    <div class="bolt-pattern" role="img" aria-label="Faint repeating lightning bolt pattern in dark grey"></div>
    <div class="brand-mark"></div>
    <div class="wordmark">
      <span class="wordmark__name">BRIGHTVALE</span>
      <span class="wordmark__sub">ELECTRICAL</span>
    </div>
  </section>

  <section class="card card--back" aria-label="Business card back">
    <div class="brand-mark"></div>
    <div class="wordmark">
      <span class="wordmark__name">BRIGHTVALE</span>
      <span class="wordmark__sub">ELECTRICAL</span>
    </div>
    <div class="contact">
      <p class="contact__name">DAMIAN HOLLOWAY</p>
      <p class="contact__licence">LIC E871302</p>
      <div class="contact__lines">
        <p class="contact__line"><span class="contact__label">p.</span> 0219647381</p>
        <p class="contact__line"><span class="contact__label">e.</span> info@brightvaleelectrical.example.nz</p>
      </div>
      <div class="contact__rule"></div>
      <p class="contact__services">Domestic Commercial<br>Industrial Electricians</p>
    </div>
  </section>
</div>
</body>
</html>
```